Steady at Heart: Renew Your Team Through the 6 Habits of Balance

I'm looking for a design that is clean, like the book "Look Sideways" by Milo Brecken. The book is about the principles of organic farming so I am looking for a color scheme that fits that image.
https://www.pagelantern.example/Look-Sideways-Value-Seeing-Other-ebook/dp/Q47K520ZTR/ref=sr_1_3?crid=58XQ2PL07ZV4M&keywords=milo+brecken&qid=1638739111&s=books&sprefix=milo+%2Cstripbooks%2C371&sr=1-3

I don't want a dark color scheme. I prefer a white or cream book with a bold font.

This book is a good example of what I am looking for:

https://www.pagelantern.example/Lamp-Small-Notes-Painting-Days/dp/0912736458/ref=rtpb_2/731-5529043-4417082?pd_rd_w=mq8z3&pf_rd_p=21c9e047-385b-4f7d-a1c2-6e30b8d7f914&pf_rd_r=KP3T8QZ2207LM4NX1VA5&pd_rd_r=e63a1f20-7c4d-4a91-b5e8-09f2d1c7a6e3&pd_rd_wg=3kR2x&pd_rd_i=0912736458&psc=1

Target Market(s)

CEOs and business owners who want to increase the trust in their brands

Industry/Entity Type

Management and Leadership

Colors
00AB8E
00BBA5
67D7C9
C6EFE9
E9F9F6
59FF00
82FF00
B8FF75
E3FFCB
F4FFEA
FFF300
FFF600
FEFA6F
FFFEC7
FFFEE8
FFC000
F8CF3A
FAE287
FDF2CF
FEFAEE

Requirements
Must have
• Author's name is: Harold Vesterby
Nice to have
• I have indicated some books that I like. I would be good to have a simple image such as an apple core or the earth's core or some other image of "core" but not absolutely necessary.
Should not have
• I don't want it to have a dark cover or be too heavy

```html
<!DOCTYPE html>
<html lang="en">
<head>
<meta charset="utf-8">
<title>Steady at Heart — Harold Vesterby</title>
<link href="https://fonts.googleapis.com/css2?family=Jost:ital,wght@0,400;0,500;0,600;1,400&display=swap" rel="stylesheet">
<style>
  :root {
    --paper: #ffffff;
    --ink: #171717;
    --leaf-deep: #7aae0f;
    --leaf-bright: #9bd614;
    --apple-light: #a6dc4a;
    --apple-mid: #6fb82a;
    --apple-shadow: #dcdcdc;
    --core-flesh: #eef3d2;
    --core-skin: #9cc44f;
  }
  * { margin: 0; padding: 0; box-sizing: border-box; }
  html, body {
    width: 800px;
    height: 1200px;
    overflow: hidden;
    background: var(--paper);
  }
  .cover {
    position: relative;
    width: 800px;
    height: 1200px;
    background: var(--paper);
    font-family: "Jost", "Futura", sans-serif;
    color: var(--ink);
  }
  .cover-type {
    position: absolute;
    inset: 0;
  }
  .title-word { font-family: "Jost", "Futura", sans-serif; }
  .title-lead { font-weight: 600; }
  .title-link { font-weight: 500; fill: var(--ink); }
  .title-main { font-weight: 500; fill: var(--ink); }
  .subtitle {
    font-family: "Jost", "Futura", sans-serif;
    font-size: 31px;
    fill: var(--ink);
  }
  .subtitle-lead { font-weight: 400; }
  .subtitle-accent { font-weight: 400; font-style: italic; }
  .author-name {
    font-family: "Jost", "Futura", sans-serif;
    font-weight: 500;
    font-size: 54px;
    fill: var(--ink);
  }
  .artwork {
    position: absolute;
  }
  .artwork-apple {
    left: 138px;
    top: 728px;
    width: 248px;
    height: 320px;
    border-radius: 48% 48% 46% 46%;
    background: radial-gradient(ellipse at 45% 42%, var(--apple-light) 0%, var(--apple-mid) 58%, rgba(111,184,42,0) 72%),
                radial-gradient(ellipse at 50% 96%, var(--apple-shadow) 0%, rgba(255,255,255,0) 40%);
  }
  .artwork-core {
    left: 432px;
    top: 752px;
    width: 222px;
    height: 290px;
    border-radius: 40%;
    background: radial-gradient(ellipse at 50% 50%, var(--core-flesh) 0%, var(--core-flesh) 40%, var(--core-skin) 62%, rgba(156,196,79,0) 74%);
  }
</style>
</head>
<body>
  <main class="cover">
    <svg class="cover-type" width="800" height="1200" viewBox="0 0 800 1200" xmlns="http://www.w3.org/2000/svg">
      <defs>
        <linearGradient id="leafGradient" x1="0" y1="0" x2="1" y2="0">
          <stop offset="0" stop-color="var(--leaf-deep)"/>
          <stop offset="0.5" stop-color="var(--leaf-bright)"/>
          <stop offset="1" stop-color="var(--leaf-deep)"/>
        </linearGradient>
      </defs>

      <text class="title-word title-lead" x="400" y="198" font-size="166" text-anchor="middle"
            textLength="672" lengthAdjust="spacingAndGlyphs" fill="url(#leafGradient)">STEADY</text>

      <text class="title-word title-link" x="400" y="352" font-size="100" text-anchor="middle">AT</text>

      <text class="title-word title-main" x="400" y="612" font-size="250" text-anchor="middle"
            textLength="672" lengthAdjust="spacingAndGlyphs">HEART</text>

      <text class="subtitle subtitle-lead" x="400" y="664" text-anchor="middle">Renew Your Team Through the</text>
      <text class="subtitle subtitle-accent" x="400" y="701" text-anchor="middle">6 Habits of Balance</text>

      <text class="author-name" x="400" y="1132" text-anchor="middle"
            textLength="610" lengthAdjust="spacing">HAROLD VESTERBY</text>
    </svg>

    <div class="artwork artwork-apple" role="img" aria-label="Photograph of a whole fresh green apple with a leaf on its stem"></div>
    <div class="artwork artwork-core" role="img" aria-label="Photograph of an eaten green apple core with its stem"></div>
  </main>
</body>
</html>
```